Trifold Pamphlet/leaflet design for Tide Nest Retreats, Trainings and Community

We would like to create a trifold leaflet showcasing Tide Nest and our retreats for promotional purposes. Tide Nest is an Australian based global company offering life-changing retreats, online trainings and inspired community within the health, wellness, personal development and human potential space.
We will use the 6 pages to showcase the Front cover with logo and tagline/keywords - Explore, Play, Connect,
Back Cover can have contact details, website , social media etc and the other 4 pages to detail
1. who Tide Nest is, what we are about, pics of the team
2. Our retreats including pictures of the Retreat Centre
3. Our Online Trainings
4 Our Inspired Community.
Each page to include text and images that I will provide shortly. Look is to align with colour palate and feel of logo and website - preview of website, in progress, here - https://kimpagecraft.sampleeditorhub.com/site/7a2c9e14/?preview=true&insitepreview=true
Little less black in the leaflets than on the website perhaps
Text is to be in poppins font.
Please advise of any questions, will forward images and text early next week - awaiting our photographer!
Best, Ned
Target Market(s)
35-55, senior leaders, business owners. 65% female, 35% male. Interested in yoga, wellbeing, peak performance, mindfulness.
Industry/Entity Type
Health And Wellness
Look and feel

```html
<!DOCTYPE html>
<html lang="en">
<head>
<meta charset="utf-8">
<title>Tide Nest – Trifold Outside</title>
<link rel="stylesheet" href="https://fonts.googleapis.com/css2?family=Poppins:wght@300;400;500;600;700;800&display=swap">
<style>
  :root{
    --stage:#a8a8a8;
    --navy:#1e1b33;
    --navy-deep:#15132a;
    --orange:#f3913a;
    --teal:#7fd0c3;
    --teal-strong:#2fb19e;
    --ink:#1f1d2b;
    --muted:#6b6b73;
    --paper:#ffffff;
    --paper-soft:#f3f3f4;
    --rule:#3a3a44;
  }
  *{box-sizing:border-box;margin:0;padding:0}
  html,body{width:773px;height:1200px;overflow:hidden}
  body{background:var(--stage);font-family:"Poppins",sans-serif;color:var(--ink);position:relative}

  .brochure{position:absolute;left:20px;top:314px;width:733px;height:572px;display:flex;box-shadow:0 2px 6px rgba(0,0,0,.25)}
  .panel{position:relative;height:100%;display:flex;flex-direction:column;align-items:center;text-align:center;overflow:hidden}
  .panel--team{width:245px;background:var(--paper-soft)}
  .panel--contact{width:244px;background:var(--paper)}
  .panel--cover{width:244px;background:var(--paper-soft)}

  .panel__footer{position:absolute;left:0;right:0;bottom:0;height:27px;display:flex;align-items:center;justify-content:center;font-size:6.6px;color:#fff;letter-spacing:.1px}
  .panel__footer--navy{background:var(--navy)}
  .panel__footer--teal{background:var(--teal)}

  .headline{font-weight:700;font-size:15.6px;line-height:1.33;margin-top:22px}
  .headline .accent{color:var(--orange)}
  .headline .cool{color:var(--teal)}
  .headline .dark{color:var(--ink)}
  .divider{width:50px;height:1px;background:var(--rule);margin:11px auto 10px}
  .body-copy{font-size:8.4px;line-height:1.3;color:#333;padding:0 18px}

  .pill{margin-top:14px;background:var(--teal);color:#fff;font-weight:600;font-size:13px;padding:2px 12px;border-radius:7px;box-shadow:0 3px 4px -2px rgba(0,0,0,.25)}

  .team{display:grid;grid-template-columns:92px 92px;column-gap:10px;row-gap:12px;margin-top:18px}
  .member{display:flex;flex-direction:column;align-items:center}
  .member__photo{width:88px;height:88px;border-radius:50%;background:radial-gradient(circle at 50% 40%,#c9b9aa 0,#8f7c6c 45%,#e4e4e6 46%,#e4e4e6 100%)}
  .member__name{font-weight:600;font-size:7.8px;margin-top:9px;white-space:nowrap}
  .member__role{font-size:5.8px;color:var(--muted);margin-top:1px}

  .offer{margin-top:24px;width:172px;border-radius:8px;overflow:hidden;box-shadow:0 4px 4px -3px rgba(0,0,0,.3)}
  .offer__regular{background:var(--teal-strong);color:#fff;font-weight:700;font-size:15px;padding:3px 0 2px}
  .offer__deal{background:var(--orange);color:#fff;font-weight:600;font-size:9.6px;line-height:1.35;padding:4px 0 5px}

  .wordmark{font-family:"Poppins",sans-serif;font-weight:300;letter-spacing:2px;white-space:nowrap}
  .wordmark--contact{font-size:25px;color:var(--ink);margin-top:44px}
  .cta{font-weight:600;font-size:11.4px;color:var(--teal-strong);margin-top:8px}
  .icons{display:flex;gap:18px;margin-top:12px}
  .icons svg{width:14px;height:14px;stroke:var(--orange);fill:none;stroke-width:1.3}
  .address{font-size:9.7px;line-height:1.45;color:#2a2a33;margin-top:12px}
  .social{display:flex;gap:14px;margin-top:12px}
  .social span{width:10px;height:10px;border-radius:50%;background:#c9c9cd}

  .cover__sky{position:absolute;left:0;top:0;width:100%;height:304px;background:linear-gradient(180deg,var(--navy-deep),var(--navy))}
  .wordmark--cover{position:relative;font-size:29px;color:#fff;margin-top:38px}
  .cover__photo{position:absolute;left:4px;top:118px;width:236px;height:236px;border-radius:50%;border:4px solid #fff;background:radial-gradient(circle at 50% 62%,#f6b56b 0,#c77a3a 10%,#2d6c77 32%,#123a47 62%,#0c1f2b 100%)}
  .tagline{position:absolute;left:0;right:0;top:376px;font-weight:800;line-height:.95}
  .tagline__explore{display:block;color:var(--orange);font-size:37px;letter-spacing:-.5px}
  .tagline__play{display:block;color:var(--teal);font-size:62px;letter-spacing:1px}
  .tagline__connect{display:block;color:var(--teal-strong);font-size:31.5px}
</style>
</head>
<body>
<main class="brochure">

  <section class="panel panel--team">
    <h2 class="headline">
      <span class="accent">Neuroscience<br>Based Training To Help</span><br>
      <span class="dark">You Accomplish More,<br>In Less Time, With<br>Greater Ease</span>
    </h2>
    <div class="divider"></div>
    <p class="body-copy">Our peak performance training is designed to help entrepreneurs, leaders and knowledge workers perform better than ever, under any conditions.</p>
    <div class="pill">Meet The Team</div>
    <div class="team">
      <div class="member"><div class="member__photo" role="img" aria-label="Portrait photo of team member"></div><div class="member__name">Omar Bellweather</div><div class="member__role">Managing Director</div></div>
      <div class="member"><div class="member__photo" role="img" aria-label="Portrait photo of team member"></div><div class="member__name">Lena Marrick</div><div class="member__role">Director</div></div>
      <div class="member"><div class="member__photo" role="img" aria-label="Portrait photo of team member"></div><div class="member__name">Theo Lindqvist</div><div class="member__role">Director</div></div>
      <div class="member"><div class="member__photo" role="img" aria-label="Portrait photo of team member"></div><div class="member__name">Priya Castell</div><div class="member__role">Marketing Manager</div></div>
    </div>
    <div class="panel__footer panel__footer--navy">www.kimpagecraft.sampleeditorhub.com</div>
  </section>

  <section class="panel panel--contact">
    <h2 class="headline">
      <span class="accent">Facilitating</span><br>
      <span class="cool">Flow For Whole<br>Human Thriving</span>
    </h2>
    <div class="divider"></div>
    <p class="body-copy">Life-changing retreats, online trainings &amp; inspired community for personal and organizational peak performance and wellbeing.</p>
    <div class="offer">
      <div class="offer__regular">NORMALLY $995</div>
      <div class="offer__deal">For a limited time only, $345<br>SAVE $650.00</div>
    </div>
    <div class="wordmark wordmark--contact">TIDE NEST</div>
    <div class="cta">Get In touch with Us</div>
    <div class="icons">
      <svg viewBox="0 0 16 16" aria-label="Location"><path d="M8 15s5-5 5-8.5A5 5 0 0 0 3 6.5C3 10 8 15 8 15z"/><circle cx="8" cy="6.5" r="1.8"/></svg>
      <svg viewBox="0 0 16 16" aria-label="Email"><rect x="1.5" y="3.5" width="13" height="9" rx="1"/><path d="M1.5 4l6.5 5 6.5-5"/></svg>
      <svg viewBox="0 0 16 16" aria-label="Phone"><path d="M4 1.5l2.3 3-1.3 1.6a8 8 0 0 0 4.9 4.9l1.6-1.3 3 2.3-1.2 2.2C8 14.5 1.5 8 1.8 2.7z"/></svg>
      <svg viewBox="0 0 16 16" aria-label="Website"><circle cx="8" cy="8" r="6.5"/><ellipse cx="8" cy="8" rx="2.8" ry="6.5"/><path d="M1.5 8h13M2.5 4.8h11M2.5 11.2h11"/></svg>
    </div>
    <p class="address">10 Street Name, City Name<br>Country, Zip Code<br>555 555 555<br>example@mail.com</p>
    <div class="social"><span></span><span></span><span></span></div>
    <div class="panel__footer panel__footer--teal">www.kimpagecraft.sampleeditorhub.com</div>
  </section>

  <section class="panel panel--cover">
    <div class="cover__sky"></div>
    <div class="wordmark wordmark--cover">TIDE NEST</div>
    <div class="cover__photo" role="img" aria-label="Photo of a hand holding a glowing light bulb with a brain inside"></div>
    <h1 class="tagline">
      <span class="tagline__explore">EXPLORE</span>
      <span class="tagline__play">PLAY</span>
      <span class="tagline__connect">CONNECT</span>
    </h1>
    <div class="panel__footer panel__footer--navy">www.kimpagecraft.sampleeditorhub.com</div>
  </section>

</main>
</body>
</html>
```